Verdant Loop Advisors, LLC

I am looking for a simple, clear layout with my logo prominent and embossed, on the best quality card stock available. I would like the business name and phone number included on the card as well......I dont want my name anywhere on the card and I would like my logo embossed on the card......something simple with a white back......open to designs as long as they go along with recycling symbols and green type stuff.....The address, website, cell number, fax number, and email are listed below

5374 Tillbury Fenwood Road
Brenmoor, MD 20999

c. 240.555.0143 f. 240.555.0187
e. sales@verdantloopadvisors.example
w. www.verdantloopadvisors.example

Industry/Entity Type

Recycling

```html
<!DOCTYPE html>
<html lang="en">
<head>
<meta charset="utf-8">
<title>Verdant Loop Advisors, LLC — Business Card</title>
<link href="https://fonts.googleapis.com/css2?family=Arimo:wght@400;700&display=swap" rel="stylesheet">
<style>
  :root {
    --backdrop: #a3a3a3;
    --card-white: #f2f2f0;
    --card-green: #125020;
    --ink-dark: #1d1a18;
    --ink-light: #ffffff;
    --shadow: rgba(0, 0, 0, 0.22);
  }
  * { box-sizing: border-box; margin: 0; padding: 0; }
  html, body {
    width: 1200px;
    height: 720px;
    overflow: hidden;
    background: var(--backdrop);
    font-family: "Arimo", Arial, sans-serif;
  }
  .sheet {
    position: relative;
    width: 1200px;
    height: 720px;
    display: flex;
    align-items: center;
    justify-content: center;
    gap: 50px;
  }
  .card {
    position: relative;
    width: 525px;
    height: 300px;
    box-shadow: 0 6px 18px var(--shadow);
  }
  .card--front {
    background: var(--card-white);
    display: flex;
    align-items: center;
    justify-content: center;
  }
  .brand {
    display: flex;
    align-items: center;
    gap: 16px;
  }
  .brand__square {
    width: 44px;
    height: 44px;
    background: var(--card-green);
  }
  .brand__name {
    font-weight: 700;
    font-size: 28px;
    letter-spacing: 0.02em;
    color: var(--ink-dark);
  }
  .card--back {
    background: var(--card-green);
    color: var(--ink-light);
  }
  .card--back .brand {
    position: absolute;
    top: 34px;
    left: 36px;
  }
  .card--back .brand__square {
    width: 30px;
    height: 30px;
    background: var(--ink-light);
  }
  .card--back .brand__name {
    color: var(--ink-light);
    font-size: 18px;
  }
  .contact {
    position: absolute;
    right: 30px;
    bottom: 34px;
    list-style: none;
    font-size: 13px;
    line-height: 1.3;
    text-align: right;
  }
  .contact__row {
    display: flex;
    align-items: center;
    justify-content: flex-end;
    gap: 14px;
  }
  .contact__row + .contact__row { margin-top: 2px; }
  .contact__row--gap { margin-top: 12px !important; }
  .contact__icon {
    width: 11px;
    height: 11px;
    flex: none;
    fill: var(--ink-light);
  }
</style>
</head>
<body>
<main class="sheet">
  <section class="card card--front" aria-label="Card front">
    <div class="brand">
      <span class="brand__square"></span>
      <span class="brand__name">Verdant Loop Advisors, LLC</span>
    </div>
  </section>

  <section class="card card--back" aria-label="Card back">
    <div class="brand">
      <span class="brand__square"></span>
      <span class="brand__name">Verdant Loop Advisors, LLC</span>
    </div>
    <ul class="contact">
      <li class="contact__row">
        <span>5374 Tillbury Fenwood Road<br>Brenmoor, MD 20999</span>
        <svg class="contact__icon" viewBox="0 0 12 12"><path d="M6 1 0 6h2v5h3V8h2v3h3V6h2z"/></svg>
      </li>
      <li class="contact__row contact__row--gap">
        <span>240.555.0143</span>
        <svg class="contact__icon" viewBox="0 0 12 12"><path d="M2.5 0.5 4.5 3 3.3 4.3c.7 1.7 2 3 3.7 3.7L8.3 6.8 11 8.8 9.8 11.3C5 11 1 7 0.7 2.2z"/></svg>
      </li>
      <li class="contact__row">
        <span>240.555.0187</span>
        <svg class="contact__icon" viewBox="0 0 12 12"><path d="M3 0h5v3H3zM0 4h12v6H0zm2 7h8v1H2z"/></svg>
      </li>
      <li class="contact__row contact__row--gap">
        <span>sales@verdantloopadvisors.example</span>
        <svg class="contact__icon" viewBox="0 0 12 12"><path d="M0 2h12v8H0zm1 1v.4l5 3.3 5-3.3V3z"/></svg>
      </li>
      <li class="contact__row">
        <span>www.verdantloopadvisors.example</span>
        <svg class="contact__icon" viewBox="0 0 12 12"><circle cx="6" cy="6" r="5.5"/></svg>
      </li>
    </ul>
  </section>
</main>
</body>
</html>
```